Business card for Autism Consultancy

I need a double-sided business card for Brightpath Kinder Consultancy
Please try to use the colours and graphics in line with our website www.brightpathkinder.nz
Front side
Logo and the name of the company – Brightpath Kinder Consultancy
We use Child-Centred, Modern and Innovative approaches
Teaching autistic children to bond, laugh and play
www.brightpathkinder.nz
info@brightpathkinder.nz
phone +64 09 37 815 66
Back side
Photo
Orla Fennimore
Founder
Postgraduate Autism (Children) Specialist (with Merit)
Qualified by the Faculty of Learning Support and Wellbeing Studies (FLSW), University of Thornvale
orla@brightpathkinder.nz
phone +64 937 815 66
mobile: +64 20 6283 9145
Please do not convert the text fields to outlines, i.e. I need to be able to edit any text after.
The final design should be either in Adobe Illustrator or Adobe Photoshop format.
The Specs for the business card are:
Full Bleed Size
94 x 58 mm
1110 x 685 pixels
Document Trim Size
91 x 55 mm
1075 x 650 pixels

```html
<!DOCTYPE html>
<html lang="en">
<head>
<meta charset="utf-8">
<title>Brightpath Kinder Consultancy – Business Cards</title>
<link href="https://fonts.googleapis.com/css2?family=Lato:wght@400;700&display=swap" rel="stylesheet">
<style>
  :root{
    --navy:#1f2f6b;
    --yellow:#f4cd1c;
    --white:#ffffff;
    --grey:#6d7280;
    --backdrop:#3a3330;
    --photo-a:#d9b59c;
    --photo-b:#5a3f33;
  }
  *{box-sizing:border-box;margin:0;padding:0}
  html,body{width:1200px;height:716px;overflow:hidden}
  body{background:var(--backdrop);font-family:"Lato",Arial,sans-serif;position:relative}
  .card{position:absolute;top:195px;width:540px;height:327px;overflow:hidden;box-shadow:0 10px 24px rgba(0,0,0,.45)}
  .card--front{left:40px;background:var(--navy);color:var(--white)}
  .card--back{left:620px;background:var(--white);color:var(--navy)}
  .card__art{position:absolute;inset:0;width:100%;height:100%}

  .brand{position:absolute;display:flex;align-items:center;gap:10px}
  .brand__dot{width:24px;height:24px;border-radius:50%;background:var(--yellow);flex:none}
  .brand__name{font-weight:700;letter-spacing:.3px}
  .card--front .brand{left:118px;top:118px}
  .card--front .brand__name{font-size:22px;color:var(--white)}
  .card--back .brand{left:34px;top:28px}
  .card--back .brand__name{font-size:15px;color:var(--navy)}

  .contact{position:absolute;list-style:none;font-size:13px;line-height:1.55}
  .contact li{display:flex;align-items:center;gap:7px}
  .contact svg{width:12px;height:12px;flex:none}
  .card--front .contact{left:34px;bottom:26px}
  .card--back .contact{right:34px;bottom:20px;color:var(--white);text-align:right}
  .card--back .contact li{justify-content:flex-end}

  .person{position:absolute;left:34px;top:76px}
  .person__name{font-size:20px;font-weight:700;text-transform:uppercase;letter-spacing:.5px;color:var(--navy)}
  .person__role,.person__title{font-size:12px;color:var(--grey);line-height:1.4}
  .person__role{margin-top:2px}
</style>
</head>
<body>

<section class="card card--front" aria-label="Business card front">
  <div class="brand">
    <span class="brand__dot"></span>
    <span class="brand__name">Brightpath Kinder Consultancy</span>
  </div>
  <ul class="contact">
    <li><svg viewBox="0 0 12 12"><path d="M3 1l2 2-1 1.5c.8 1.6 1.9 2.7 3.5 3.5L9 7l2 2-1.5 2C5 11 1 7 1 2.5z" fill="var(--yellow)"/></svg>+64 09 37 815 66</li>
    <li><svg viewBox="0 0 12 12"><rect x="1" y="2.5" width="10" height="7" fill="none" stroke="var(--yellow)" stroke-width="1.2"/><path d="M1 3l5 3.5L11 3" fill="none" stroke="var(--yellow)" stroke-width="1.2"/></svg>info@brightpathkinder.nz</li>
    <li><svg viewBox="0 0 12 12"><circle cx="6" cy="6" r="4.8" fill="none" stroke="var(--yellow)" stroke-width="1.2"/><path d="M1.2 6h9.6M6 1.2c-2.4 3-2.4 6.6 0 9.6M6 1.2c2.4 3 2.4 6.6 0 9.6" fill="none" stroke="var(--yellow)" stroke-width="1"/></svg>www.brightpathkinder.nz</li>
  </ul>
</section>

<section class="card card--back" aria-label="Business card back">
  <svg class="card__art" viewBox="0 0 540 327" aria-hidden="true">
    <path d="M0 150 C80 205 190 222 300 222 L540 236 L540 327 L0 327 Z" fill="var(--navy)"/>
    <path d="M0 143 C80 198 190 215 300 215 L540 229" fill="none" stroke="var(--yellow)" stroke-width="5"/>
  </svg>
  <svg class="card__art" viewBox="0 0 540 327">
    <defs>
      <radialGradient id="photoTone" cx="50%" cy="45%" r="60%">
        <stop offset="0" stop-color="var(--photo-a)"/>
        <stop offset="1" stop-color="var(--photo-b)"/>
      </radialGradient>
    </defs>
    <circle cx="405" cy="168" r="80" fill="var(--white)" stroke="var(--yellow)" stroke-width="3"/>
    <circle cx="405" cy="168" r="74" fill="url(#photoTone)" role="img" aria-label="Portrait photo of Orla Fennimore"/>
  </svg>

  <div class="brand">
    <span class="brand__dot"></span>
    <span class="brand__name">Brightpath Kinder Consultancy</span>
  </div>

  <div class="person">
    <h1 class="person__name">Orla Fennimore</h1>
    <p class="person__role">Founder</p>
    <p class="person__title">Postgraduate Autism<br>(Children) Specialist (with Merit)</p>
  </div>

  <ul class="contact">
    <li>+64 937 815 66<svg viewBox="0 0 12 12"><path d="M3 1l2 2-1 1.5c.8 1.6 1.9 2.7 3.5 3.5L9 7l2 2-1.5 2C5 11 1 7 1 2.5z" fill="var(--yellow)"/></svg></li>
    <li>+64 20 6283 9145<svg viewBox="0 0 12 12"><rect x="3" y="1" width="6" height="10" rx="1" fill="none" stroke="var(--yellow)" stroke-width="1.2"/><circle cx="6" cy="9" r=".8" fill="var(--yellow)"/></svg></li>
    <li>orla@brightpathkinder.nz<svg viewBox="0 0 12 12"><rect x="1" y="2.5" width="10" height="7" fill="none" stroke="var(--yellow)" stroke-width="1.2"/><path d="M1 3l5 3.5L11 3" fill="none" stroke="var(--yellow)" stroke-width="1.2"/></svg></li>
  </ul>
</section>

</body>
</html>
```